Business Card 85x40mm - Freelance audio mixing / live event operator

I am a freelance audio operator working in live events. Mostly corporate events mixing sound for a range of entertainment, awards nights and functions. I need a new card to give to perspective clients.

The final design will convey bold professionalism with a general dark vibe. Looking for dark-ish background with some smatterings of colour added.

I have attatched my old BC for an idea of what I have liked in the past. Id like a more modern updated design (that circular design on the back is not my logo it is just a picture I found that resembled sound} . For an added element possibly a mixture of some playful colours in a way that resembles an audio wave form or sound.

I have attached a photo called "audio software" with some colourful squiggly lines; maybe incorporate elements of that into into design
Updates

Added extra $ to project Damn Pixel herds fees are unreasonable

Target Market(s)

Mostly corporate clients

Industry/Entity Type

Events

Contact Information for Business Card

Corwin Blaylock
Sound | FOH | Monitors | Systems | Corporate

Digital Audio Mixing Specialist, Live Event Technical Professional,

corwinblaylock@mailvane.net, +61 408 315 927

Colors
ec1f27
ffc214
9bcb3c
6b449b

Requirements
Must have
• Dark theme
• 85x40mm dimensions
Nice to have
• some sort of imagery or design to reflect audio/sound

```html
<!DOCTYPE html>
<html lang="en">
<head>
<meta charset="utf-8">
<title>Corwin Blaylock – Business Card</title>
<link rel="stylesheet" href="https://fonts.googleapis.com/css2?family=Mulish:wght@300;400;700&display=swap">
<style>
  :root {
    --canvas: #ffffff;
    --card: #000000;
    --ink: #ffffff;
    --violet: #6b449b;
    --violet-light: #b39ad6;
    --violet-pale: #e6dcf3;
  }
  * { margin: 0; padding: 0; box-sizing: border-box; }
  html, body {
    width: 1200px; height: 1000px; overflow: hidden;
    background: var(--canvas);
    font-family: "Mulish", sans-serif;
    color: var(--ink);
  }
  .card {
    position: absolute; left: 303px; width: 632px; height: 298px;
    background: var(--card); overflow: hidden;
  }
  .card--front { top: 190px; }
  .card--back { top: 514px; height: 297px; }

  .monogram {
    position: absolute; top: 24px; left: 0; width: 100%;
    text-align: center; font-weight: 700; font-size: 44px; line-height: 1;
    letter-spacing: -1px; color: var(--ink);
  }
  .name {
    position: absolute; top: 96px; left: 0; width: 100%;
    text-align: center; font-weight: 700; font-size: 26px;
  }
  .wave {
    position: absolute; left: 0; width: 100%;
  }
  .wave--front {
    top: 155px; height: 70px;
    background:
      linear-gradient(180deg, transparent 0%, rgba(107,68,155,0.55) 30%, var(--violet-pale) 50%, rgba(107,68,155,0.55) 70%, transparent 100%);
    -webkit-mask: linear-gradient(90deg, transparent 0%, #000 3%, #000 97%, transparent 100%);
            mask: linear-gradient(90deg, transparent 0%, #000 3%, #000 97%, transparent 100%);
  }
  .wave--back {
    top: 92px; height: 110px;
    background: radial-gradient(ellipse 55% 50% at 50% 50%, rgba(107,68,155,0.9) 0%, rgba(107,68,155,0.45) 55%, transparent 100%);
  }
  .contact {
    position: absolute; top: 248px; left: 0; width: 100%;
    display: flex; justify-content: center; align-items: center; gap: 30px;
    font-size: 20px; font-weight: 400;
  }
  .contact__item { display: flex; align-items: center; gap: 12px; }
  .contact__icon { display: block; fill: none; stroke: var(--ink); }

  .services {
    position: absolute; top: 40px; left: 0; width: 100%;
    text-align: center; font-size: 26px; font-weight: 300;
  }
  .roles {
    position: absolute; top: 221px; left: 0; width: 100%;
    text-align: center; font-size: 22px; font-weight: 300; line-height: 30px;
  }
</style>
</head>
<body>
  <section class="card card--front">
    <div class="monogram">CB</div>
    <h1 class="name">Corwin Blaylock</h1>
    <div class="wave wave--front" role="img" aria-label="Purple audio waveform running across the card"></div>
    <div class="contact">
      <span class="contact__item">
        <svg class="contact__icon" width="24" height="16" viewBox="0 0 24 16" aria-hidden="true">
          <rect x="1" y="1" width="22" height="14" fill="#fff" stroke="none"/>
          <path d="M1 1 L12 9 L23 1 M1 15 L9 7 M23 15 L15 7" stroke="#000" stroke-width="1.5"/>
        </svg>
        corwinblaylock@mailvane.net
      </span>
      <span class="contact__item">
        <svg class="contact__icon" width="16" height="24" viewBox="0 0 16 24" aria-hidden="true">
          <rect x="1.5" y="1.5" width="13" height="21" rx="2.5" stroke-width="2"/>
          <line x1="2" y1="17" x2="14" y2="17" stroke-width="1.5"/>
          <circle cx="8" cy="19.8" r="1.2" fill="#fff" stroke="none"/>
        </svg>
        +61 408 315 927
      </span>
    </div>
  </section>

  <section class="card card--back">
    <p class="services">Sound | FOH | Monitors | Systems | Corporate</p>
    <div class="wave wave--back" role="img" aria-label="Tangled purple sound lines forming a wave"></div>
    <p class="roles">Digital Audio Mixing Specialist<br>Live Event Technical Professional</p>
  </section>
</body>
</html>
```